Meridian Counsel Society of Ohio (MCS) Gala 2023

We need an invitation ASAP for the MCS's 73rd annual Scholarship Ball that incorporates the logo in a more elegant, creative, & streamlined design than last year.

We want a corporate, not wedding, feel and need to keep the costs down because this is a fundraiser for law school scholarship recipients. Keep envelope sizes standard. An embossed sticker or wax seal could be an option.

Incorporate the color terracotta the invitation stand out as a stylish, yet serious affair. Utilize cream writing on terracotta for the outer fold (cover) which will say " Please join us to celebrate (in discrete letters) and then Filotimo and the definition of Filotimo.

The inside of the folded invitation will be cream, but with terracotta accents (Like a border) *Please use the new logo I just added today with books. Also, please use the PDF that I just attached for the information on the inside of the invitation.

Put "Black Tie Optional" in a corner in smaller letters.

Put the officers names on the back of the invitation. Use white ink for their names and titles.

Use a Greek letter font to write the word Filotimo in Greek letters, and write our definition of the word filotimo in English below.

Return address for the back of the envelope is:
It would be okay to add a logo on the envelope.
Mr. and Mrs. Talbot Verhoeven
848 Quarrow Lane
Irvine, California 71000

Target Market(s)

lawyers and judges

Industry/Entity Type

Legal

Font styles to use
Decorative
Other font styles liked:
• Please emphasize the words Scholarship Ball so they are larger and stand out.

Colors

Designer to choose colors to be used in the design.

Requirements
Must have
• The word Filotimo written in a Greek font, but everything else in English. See attached photo for how to write in Greek. Include Accent mark.
Nice to have
• Creative envelopes with writing in dark brown or terracotta.
Should not have
• The officers names on the front or the inside of the invitation. They should be on the back.

```html
<!DOCTYPE html>
<html lang="en">
<head>
<meta charset="utf-8">
<title>MCS Scholarship Ball Invitation – Option 2</title>
<link rel="stylesheet" href="https://fonts.googleapis.com/css2?family=Poppins:ital,wght@0,400;0,500;0,700;1,500&family=Old+Standard+TT&family=Josefin+Sans:wght@600&family=Great+Vibes&display=swap">
<style>
  :root {
    --slate-dark: #2e3744;
    --slate-light: #434f5c;
    --terracotta: #d4603a;
    --cream: #fcf8d8;
    --cream-ink: #fbf1cf;
    --brown: #3a1a14;
    --ink: #2b2b2b;
    --accent-red: #b8382b;
  }
  html, body {
    margin: 0;
    padding: 0;
    width: 1200px;
    height: 996px;
    overflow: hidden;
  }
  body {
    position: relative;
    background: linear-gradient(135deg, var(--slate-dark), var(--slate-light));
    font-family: "Poppins", sans-serif;
  }
  .board-title {
    position: absolute;
    left: 0; right: 0; top: 54px;
    margin: 0;
    text-align: center;
    font-weight: 700;
    font-size: 50px;
    line-height: 1;
    color: var(--terracotta);
  }
  .side-label {
    position: absolute;
    width: 200px;
    margin: 0;
    text-align: center;
    font-weight: 700;
    font-size: 32px;
    line-height: 1;
    color: var(--terracotta);
  }
  .side-label--front { left: 185px; top: 933px; }
  .side-label--back { left: 797px; top: 929px; }

  .card {
    position: absolute;
    top: 174px;
    width: 474px;
    height: 664px;
    background: var(--cream);
    overflow: hidden;
  }
  .card--front { left: 103px; }
  .card--back { left: 657px; }

  /* Cover band */
  .cover-band {
    position: absolute;
    left: 0; top: 0;
    width: 190px; height: 100%;
    background: var(--terracotta);
    color: var(--cream-ink);
    text-align: center;
  }
  .emblem {
    position: absolute;
    display: block;
  }
  .cover-band .emblem { left: 26px; top: 24px; width: 137px; height: 168px; }
  .cover-invite {
    position: absolute;
    left: 0; right: 0; top: 217px;
    font-size: 10px;
  }
  .cover-org {
    position: absolute;
    left: 0; right: 0; top: 237px;
    margin: 0;
    font-family: "Old Standard TT", serif;
    font-weight: 400;
    font-size: 20px;
    line-height: 24px;
  }
  .cover-celebrate {
    position: absolute;
    left: 0; right: 0; top: 317px;
    font-size: 9.5px;
  }
  .philotimo-word {
    position: absolute;
    left: 0; right: 0; top: 391px;
    margin: 0;
    font-family: "Old Standard TT", serif;
    font-weight: 400;
    font-size: 27px;
    line-height: 1;
  }
  .philotimo-rule {
    position: absolute;
    left: 27px; top: 434px;
    width: 134px; height: 1px;
    background: var(--cream-ink);
  }
  .philotimo-definition {
    position: absolute;
    left: 25px; top: 452px;
    width: 139px;
    margin: 0;
    font-size: 10.6px;
    line-height: 13.2px;
    text-align: justify;
  }

  /* Inside details */
  .details { position: absolute; left: 206px; top: 0; right: 0; bottom: 0; }
  .eyebrow, .event-date {
    position: absolute;
    left: 0;
    margin: 0;
    font-family: "Josefin Sans", sans-serif;
    font-weight: 600;
    font-size: 16px;
    letter-spacing: 2.2px;
    line-height: 1;
    color: var(--terracotta);
  }
  .eyebrow { top: 41px; }
  .event-date { top: 209px; }
  .event-title {
    position: absolute;
    left: -6px; top: 78px;
    margin: 0;
    font-family: "Great Vibes", cursive;
    font-weight: 400;
    color: var(--brown);
    line-height: 1;
    white-space: nowrap;
  }
  .event-title__line { display: block; font-size: 62px; }
  .event-title__line--second { padding-left: 22px; font-size: 74px; margin-top: -8px; }
  .body-text {
    position: absolute;
    left: 0;
    margin: 0;
    font-size: 11px;
    line-height: 16px;
    color: var(--ink);
  }
  .venue { top: 252px; font-weight: 500; }
  .intro { top: 318px; width: 230px; }
  .honoree { position: absolute; left: 0; }
  .honoree--first { top: 389px; }
  .honoree--second { top: 459px; }
  .honoree__name {
    margin: 0;
    font-family: "Old Standard TT", serif;
    font-weight: 400;
    font-size: 17px;
    line-height: 20px;
    color: var(--ink);
  }
  .honoree__role {
    margin: 0;
    font-size: 11px;
    line-height: 16px;
    font-weight: 500;
    color: var(--ink);
  }
  .honoree__award {
    margin: 0;
    font-size: 11px;
    line-height: 16px;
    font-style: italic;
    font-weight: 500;
    color: var(--accent-red);
  }
  .tickets { top: 552px; }
  .tickets a { color: var(--accent-red); font-style: italic; text-decoration: none; font-weight: 500; }
  .dress-code {
    position: absolute;
    right: 20px; top: 628px;
    margin: 0;
    font-size: 11px;
    font-weight: 500;
    color: var(--ink);
  }

  /* Back */
  .card--back .emblem { left: 148px; top: 113px; width: 177px; height: 220px; }
  .officers {
    position: absolute;
    left: 34px; top: 470px;
    width: 420px;
    margin: 0; padding: 0;
    list-style: none;
    display: grid;
    grid-template-columns: 234px 186px;
    row-gap: 6px;
  }
  .officer__name {
    display: block;
    font-family: "Old Standard TT", serif;
    font-size: 14.5px;
    line-height: 18px;
    color: var(--ink);
  }
  .officer__title {
    display: block;
    font-size: 9.6px;
    line-height: 15px;
    font-style: italic;
    font-weight: 500;
    color: var(--accent-red);
  }
</style>
</head>
<body>
  <h1 class="board-title">Revised Design - option 2</h1>

  <section class="card card--front" aria-label="Invitation front">
    <div class="cover-band">
      <svg class="emblem" role="img" aria-label="Emblem illustration: blindfolded justice figure holding scales and sword within a laurel wreath" viewBox="0 0 137 168">
        <rect width="137" height="168" rx="8" fill="#f3dcb8" opacity="0.35"/>
      </svg>
      <div class="cover-invite">Please join</div>
      <h2 class="cover-org">Meridian<br>Counsel Society<br>Foundation</h2>
      <div class="cover-celebrate">Celebrate</div>
      <h2 class="philotimo-word" lang="el">Φιλότιμο</h2>
      <div class="philotimo-rule"></div>
      <p class="philotimo-definition">Noun [fee-lo-tee-mo]; an ancient Greek word with a biblical roots which loosely translates to “love of honor”; an array of virtues including respect, kindness, duty, sacrifice, generosity, and hospitality; considered to be the highest of all the Greek virtues and, at its core, means doing good works for the benefit of humanity.</p>
    </div>

    <div class="details">
      <p class="eyebrow">MCS’S 73RD ANNUAL</p>
      <h2 class="event-title">
        <span class="event-title__line">Scholarship</span>
        <span class="event-title__line event-title__line--second">Ball</span>
      </h2>
      <p class="event-date">NOVEMBER 18, 2023</p>
      <p class="body-text venue">The Larkspur Grand<br>4120 Calder Ridge Road<br>Westbrook, Ohio</p>
      <p class="body-text intro">We look forward to celebrating this year’s law school scholarship recipients and the following honorees:</p>
      <div class="honoree honoree--first">
        <p class="honoree__name">Dorian Halvorsen,</p>
        <p class="honoree__role">National Officer of Corvane</p>
        <p class="honoree__award">To Be Determined, Lawyer of the Year</p>
      </div>
      <div class="honoree honoree--second">
        <p class="honoree__name">Marisol Tennant Ruehl,</p>
        <p class="honoree__role">National President of Aldermoor</p>
        <p class="honoree__award">To Be Determined, Young Lawyer of the Year</p>
      </div>
      <p class="body-text tickets">Tickets and sponsorships may be<br>purchased online at <a>www.Meridiancounsel.org</a><br>or via <a>Meridianfoundation@mailbox.example</a></p>
      <p class="dress-code">Black Tie Optional.</p>
    </div>
  </section>

  <section class="card card--back" aria-label="Invitation back">
    <svg class="emblem" role="img" aria-label="Emblem illustration: blindfolded justice figure holding scales and sword within a laurel wreath" viewBox="0 0 177 220">
      <rect width="177" height="220" rx="10" fill="#e48a63" opacity="0.45"/>
    </svg>
    <ul class="officers">
      <li><span class="officer__name">Leander J. Holloway</span><span class="officer__title">President &amp; 2023 Ball Chairperson</span></li>
      <li><span class="officer__name">Verity Okonkwo</span><span class="officer__title">Secretary</span></li>
      <li><span class="officer__name">Celia Marchetti</span><span class="officer__title">President-Elect &amp; Treasurer</span></li>
      <li><span class="officer__name">Noelle Brandt</span><span class="officer__title">Corresponding Secretary</span></li>
      <li><span class="officer__name">Hon. Gregor J. Ellison</span><span class="officer__title">First Vice President</span></li>
      <li><span class="officer__name">Ambrose Whitcombe</span><span class="officer__title">Law School Liaison</span></li>
      <li><span class="officer__name">Rosalind Ferrow Castell</span><span class="officer__title">Second Vice President</span></li>
      <li><span class="officer__name">Imogen Sterling</span><span class="officer__title">Chairwoman</span></li>
    </ul>
  </section>

  <p class="side-label side-label--front">Front</p>
  <p class="side-label side-label--back">Back</p>
</body>
</html>
```